Profesional personal website needs design and business card

I need a business card with my professional name as a logo "Orlan Vitality" for my business. I am a Wellness Coach, consultant and trainer. So it should be professional, wellness oriented and modern.

Target Market(s)

Private clients, governments, corporations. Luxury and high market.

Industry/Entity Type

Health And Wellness

Contact Information for Business Card

Orlan Vitality should be the logo

Colors

Designer to choose colors to be used in the design.

Requirements
Must have
• Orlan Vitality
• Name: Dario Montalbe
• Wellness Coach, Consultant & Trainer.
• Website: www.orlanvitality-example.com
• Phone:
• Spain (+34) 612 480 597
• (USA) +1 (555) 318 0264
Nice to have
• The most important is the design of "Orlan Vitality", as this is going to be my personal brand logo. It should be professional, wellness, high end and actual.
Should not have
• no golds, no baroque style..

```html
<!DOCTYPE html>
<html lang="en">
<head>
<meta charset="utf-8">
<title>Orlan Vitality – Business Card</title>
<link href="https://fonts.googleapis.com/css2?family=Delius&family=Arimo:wght@400&display=swap" rel="stylesheet">
<style>
  :root {
    --teal: #4e9a87;
    --ink: #404244;
    --rule: #5a5c5e;
    --card: #fbfbf9;
    --backdrop: #e6e7e8;
  }
  * { margin: 0; padding: 0; box-sizing: border-box; }
  html, body { width: 1200px; height: 936px; overflow: hidden; background: var(--backdrop); }
  .business-card {
    position: absolute; left: 80px; top: 148px;
    width: 1040px; height: 640px;
    background: var(--card);
    box-shadow: 0 6px 24px rgba(0,0,0,.12);
  }
  .brand { position: absolute; left: 45px; top: 40px; }
  .brand-dot {
    width: 64px; height: 64px; border-radius: 50%;
    background: var(--teal); margin: 0 0 34px 92px;
  }
  .brand-name {
    font-family: "Delius", cursive;
    font-size: 60px; line-height: 0.98;
    color: var(--teal); letter-spacing: 1px;
  }
  .person { position: absolute; left: 45px; top: 350px; }
  .person-name {
    font-family: "Delius", cursive;
    font-size: 48px; color: var(--teal); letter-spacing: 1px; line-height: 1.1;
  }
  .person-role {
    font-family: "Arimo", sans-serif;
    font-size: 25px; color: var(--ink); transform: scaleX(.9); transform-origin: left;
  }
  .divider {
    position: absolute; left: 45px; top: 448px; width: 950px; height: 1.5px;
    background: var(--rule);
  }
  .contacts { position: absolute; left: 45px; top: 480px; list-style: none; }
  .contacts li {
    display: flex; align-items: center; gap: 14px; height: 41px;
    font-family: "Arimo", sans-serif; font-size: 27px; color: var(--ink);
  }
  .contacts svg { width: 26px; height: 26px; flex: none; }
</style>
</head>
<body>
  <div class="business-card">
    <div class="brand">
      <div class="brand-dot"></div>
      <div class="brand-name">Orlan<br>Vitality</div>
    </div>

    <div class="person">
      <div class="person-name">Dario Montalbe</div>
      <div class="person-role">Wellness Coach, Consultant &amp; Trainer</div>
    </div>

    <div class="divider"></div>

    <ul class="contacts">
      <li>
        <svg viewBox="0 0 24 24" aria-hidden="true"><circle cx="12" cy="12" r="10.5" fill="none" stroke="#4e9a87" stroke-width="1.6"/><path d="M8.5 7.2c.5-.4 1.1-.3 1.4.2l1 1.8c.2.4.1.9-.3 1.2l-.7.5c.6 1.4 1.6 2.4 3 3l.5-.7c.3-.4.8-.5 1.2-.3l1.8 1c.5.3.6.9.2 1.4-.8 1-2 1.4-3.2.9-2.5-1-4.5-3-5.5-5.5-.5-1.2-.1-2.4.6-3.5z" fill="#4e9a87"/></svg>
        (+34) 612 480 597
      </li>
      <li>
        <svg viewBox="0 0 24 24" aria-hidden="true"><circle cx="12" cy="12" r="10.5" fill="none" stroke="#4e9a87" stroke-width="1.6"/><path d="M8.5 7.2c.5-.4 1.1-.3 1.4.2l1 1.8c.2.4.1.9-.3 1.2l-.7.5c.6 1.4 1.6 2.4 3 3l.5-.7c.3-.4.8-.5 1.2-.3l1.8 1c.5.3.6.9.2 1.4-.8 1-2 1.4-3.2.9-2.5-1-4.5-3-5.5-5.5-.5-1.2-.1-2.4.6-3.5z" fill="#4e9a87"/></svg>
        +1 (555) 318 0264
      </li>
      <li>
        <svg viewBox="0 0 24 24" aria-hidden="true"><g fill="none" stroke="#4e9a87" stroke-width="1.6"><circle cx="12" cy="12" r="10"/><ellipse cx="12" cy="12" rx="4.5" ry="10"/><path d="M2 12h20M3.5 7h17M3.5 17h17"/></g></svg>
        www.orlanvitality-example.com
      </li>
    </ul>
  </div>
</body>
</html>
```